Sign Design for Truck Repair Shop center

Need a road-side sign for a pickup truck repair shop called HaulPoint Garage. The logo is attached and should be used on the sign. The background should be white and the main part of the logo should take up a large part of the sign so it can be easily read by passing traffic. The sign is 4 feet tall by 8 feet wide. Also need to add the website address" "www.HaulPointGarage-example.com" and "Call/Text 555.382.4607"

```html
<!DOCTYPE html>
<html lang="en">
<head>
<meta charset="utf-8">
<title>HaulPoint Garage – Road Sign</title>
<link rel="stylesheet" href="https://fonts.googleapis.com/css2?family=Graduate&family=Krona+One&display=swap">
<style>
  :root {
    --brand-blue: #0a4f9c;
    --frame-grey: #8a8d90;
    --mark-grey: #85898d;
    --paper: #ffffff;
    --page: #f4f4f4;
    --icon-grey: #9a9ea2;
  }
  * { margin: 0; padding: 0; box-sizing: border-box; }
  html, body { width: 1092px; height: 1200px; overflow: hidden; background: var(--page); }
  .canvas { position: relative; width: 1092px; height: 1200px; }
  .sign {
    position: absolute; left: 46px; top: 350px; width: 1000px; height: 500px;
    background: var(--paper);
    box-shadow: 0 4px 10px rgba(0,0,0,0.25);
    overflow: hidden;
  }
  .sign-art { position: absolute; inset: 0; width: 100%; height: 100%; }
  .brand-mark {
    position: absolute; left: 450px; top: 22px; width: 100px; height: 100px;
    border-radius: 50%; background: var(--mark-grey);
  }
  .brand-name {
    position: absolute; left: 0; right: 0; top: 140px; text-align: center;
    font-family: "Graduate", serif; font-size: 62px;
    color: var(--brand-blue); line-height: 1; white-space: nowrap;
  }
  .tagline {
    position: absolute; left: 0; right: 0; top: 238px; text-align: center;
    font-family: "Graduate", serif; font-size: 30px; letter-spacing: 1px;
    color: var(--brand-blue); line-height: 1; white-space: nowrap;
  }
  .contact {
    position: absolute; left: 0; right: 0; top: 370px; text-align: center; color: var(--paper);
    font-family: "Krona One", sans-serif;
  }
  .phone { display: inline-flex; align-items: center; gap: 14px; font-size: 50px; line-height: 1; }
  .phone-icon { width: 40px; height: 40px; }
  .website { margin-top: 16px; font-size: 22px; line-height: 1; }
</style>
</head>
<body>
<div class="canvas">
  <div class="sign">
    <svg class="sign-art" viewBox="0 0 1000 500" aria-hidden="true">
      <path d="M0 345 Q500 285 1000 345 L1000 500 L0 500 Z" fill="var(--brand-blue)"/>
      <rect x="8" y="8" width="984" height="484" fill="none" stroke="var(--frame-grey)" stroke-width="2"/>
    </svg>
    <div class="brand-mark" aria-hidden="true"></div>
    <div class="brand-name">HAULPOINT GARAGE</div>
    <div class="tagline">YOUR TRUSTED KESTREL SPECIALISTS</div>
    <div class="contact">
      <div class="phone">
        <svg class="phone-icon" viewBox="0 0 24 24" aria-label="phone">
          <path fill="var(--icon-grey)" d="M6.6 10.8c1.4 2.8 3.8 5.1 6.6 6.6l2.2-2.2c.3-.3.7-.4 1-.2 1.1.4 2.3.6 3.6.6.6 0 1 .4 1 1V20c0 .6-.4 1-1 1C10.6 21 3 13.4 3 4c0-.6.4-1 1-1h3.5c.6 0 1 .4 1 1 0 1.3.2 2.5.6 3.6.1.3 0 .7-.2 1L6.6 10.8z"/>
        </svg>
        <span>555.382.4607</span>
      </div>
      <div class="website">HaulPointGarage-example.com</div>
    </div>
  </div>
</div>
</body>
</html>
```